London Based Property Finding Company - have logo already

We find property for private purchasers and investors in London, UK.  We work for the BUYER, whereas estate agencies/real estate companies work for the seller. We offer a much more personalised service to UK and overseas purchasers.

We would like the following:

*A double sided business card

*A letterhead

We have attached two versions of the logo. Each logo style is set on two different coloured backgrounds. Please choose one of the two designs, whichever you prefer or feel more comfortable with, and produce one in black and one in white background.

This applies to both pieces of stationery.

THE BUSINESS CARD:

We would like the company name placed on its own on one side of the card and the contact details and what we do on the other.

e.g.

SIDE 1:

BRAMWELL PROPERTY FINDERS

SIDE 2:

Owen Bramwell

t: 0208 394 2860

m: +44(0)7932 418 507

e: info@bramwellpropertyfinders.co.uk

w: bramwellpropertyfinders.co.uk

London Property Finders and Search Agents

I will leave the layout up to you, but a minimalist layout is preferred. If you would like to put additional detial or design on the card then that is up to, but not specified.

It is optional to have the company name on side 2, but if you do use it, please make it smaller. than on the 1st side.

The design needs to be simple, professional and not too in your face.

If you are using the black background design on side 1 for the logo, then maybe a white backgounnd can be used on side 2 with a black typeface.

The type face for the contacts details should be sans serif standard typeface. Please experiment with the desciprtion.

-

THE LETTERHEAD;

You can experiment with the layout for the letterhead. e.g logo centre aligned on the top of the page with the contact details and address at the bottom of the page OR the logo, description running along a bar on the top of the page with the contact details and website address at the bottom. Please try and experiment with this, but the less 'busy', the better.

Here is info that needs to be on the letterhead.

Bramwell Property Finders

t: 0208 394 2860

m: +44(0)7932 418 507

(PLEASE NOTE; the below company info must be placed at the bottom of the page as a footer, in small text.)

Kestrand Holdings Ltd Trading as Bramwell Property Finders, a company registered in England & Wales, No.7351926 , Registered office is 41 Hollinmoor Court, Hollinmoor Road, London, SW9 3PL, t: 0208 394 2860, m: +44(0)7932 418 507, e: info@bramwellpropertyfinders.co.uk

Best of luck!

Thank you

Dear Designer,

I have now attached the supporting files to this brief.

Thanks,

Owen Bramwell
Bramwell Property Finders

```html
<!DOCTYPE html>
<html lang="en">
<head>
<meta charset="utf-8">
<title>Bramwell Property Finders – Stationery</title>
<link rel="stylesheet" href="https://fonts.googleapis.com/css2?family=Cinzel:wght@500&family=Lato:wght@400&family=Arimo:wght@700&family=Libre+Baskerville:wght@700&display=swap">
<style>
  :root {
    --navy: #1d3461;
    --claret: #7a1020;
    --black: #000000;
    --sky: #6fc3ea;
    --paper: #ffffff;
    --edge: #333333;
  }
  * { margin: 0; padding: 0; box-sizing: border-box; }
  html, body { width: 1200px; height: 1200px; overflow: hidden; background: var(--paper); }
  .canvas { position: relative; width: 1200px; height: 1200px; }

  .sheet, .card { position: absolute; background: var(--paper); border: 1px solid var(--edge); overflow: hidden; }
  .band { position: absolute; left: 0; right: 0; }
  .rule { position: absolute; left: 0; right: 0; height: 2px; }

  .wordmark {
    position: absolute; font-family: "Cinzel", serif; font-weight: 500;
    white-space: nowrap; letter-spacing: 0.02em; color: var(--paper);
  }

  .contacts {
    position: absolute; text-align: right; font-family: "Lato", sans-serif;
    font-size: 12px; line-height: 15px; letter-spacing: 0.03em;
  }
  .contacts b { font-weight: 400; }

  .footer-text {
    position: absolute; left: 0; right: 0; text-align: center; color: var(--paper);
    font-family: "Arimo", sans-serif; font-weight: 700; font-size: 7.6px; line-height: 11.4px;
  }

  .holder { position: absolute; font-family: "Libre Baskerville", serif; font-weight: 700; font-size: 8px; letter-spacing: 0.02em; }
  .card-contacts { position: absolute; font-family: "Lato", sans-serif; font-size: 7px; line-height: 9.6px; }
  .tagline { position: absolute; right: 14px; font-family: "Lato", sans-serif; font-size: 8px; letter-spacing: 0.18em; color: var(--paper); }

  /* navy set */
  .navy .band { background: var(--navy); }
  .navy .rule { background: var(--claret); }
  .navy .contacts, .navy .card-contacts, .navy .holder { color: var(--navy); }
  .navy .contacts b, .navy .card-contacts b { color: var(--claret); }
  .navy-face { background: var(--navy); border: none; }
  .navy .card-mark { color: var(--navy); }

  /* black set */
  .mono .band { background: var(--black); }
  .mono .rule { background: var(--sky); }
  .mono .contacts, .mono .card-contacts, .mono .holder { color: var(--black); }
  .mono .contacts b, .mono .card-contacts b { color: var(--sky); }
  .mono-face { background: var(--black); border: none; }
  .mono .card-mark { color: var(--black); }
</style>
</head>
<body>
<main class="canvas">

  <!-- Navy letterhead -->
  <section class="sheet navy" style="left:23px;top:26px;width:584px;height:757px;border-right:none;">
    <div class="band" style="top:0;height:92px;"></div>
    <p class="wordmark" style="left:25px;top:32px;font-size:23px;">BRAMWELL PROPERTY FINDERS</p>
    <div class="rule" style="top:94px;"></div>
    <div class="contacts" style="right:34px;top:626px;">
      <p><b>t:</b> 0208 394 2860</p>
      <p><b>m:</b> +44(0)7932 418 507</p>
      <p><b>e:</b> info@bramwellpropertyfinders.co.uk</p>
      <p><b>w:</b> bramwellpropertyfinders.co.uk</p>
    </div>
    <div class="rule" style="top:700px;"></div>
    <div class="band" style="top:704px;height:53px;"></div>
    <div class="footer-text" style="top:714px;">
      <p>Kestrand Holdings Ltd Trading as Bramwell Property Finders, a company registered in England &amp; Wales, No.7351926</p>
      <p>Registered office is 41 Hollinmoor Court, Hollinmoor Road, London, SW9 3PL,</p>
      <p>t: 0208 394 2860, m: +44(0)7932 418 507, e: info@bramwellpropertyfinders.co.uk</p>
    </div>
  </section>

  <!-- Navy business card, front -->
  <section class="card navy-face" style="left:633px;top:32px;width:393px;height:224px;">
    <p class="wordmark" style="left:50px;top:97px;font-size:19px;">BRAMWELL PROPERTY FINDERS</p>
  </section>

  <!-- Navy business card, back -->
  <section class="card navy" style="left:780px;top:176px;width:389px;height:222px;">
    <p class="wordmark card-mark" style="left:24px;top:40px;font-size:14px;">BRAMWELL PROPERTY FINDERS</p>
    <p class="holder" style="left:24px;top:90px;">OWEN BRAMWELL</p>
    <div class="card-contacts" style="left:24px;top:114px;">
      <p><b>t:</b> 0208 394 2860</p>
      <p><b>m:</b> +44(0)7932 418 507</p>
      <p><b>e:</b> info@bramwellpropertyfinders.co.uk</p>
      <p><b>w:</b> bramwellpropertyfinders.co.uk</p>
    </div>
    <div class="rule" style="top:184px;"></div>
    <div class="band" style="top:188px;height:34px;"></div>
    <p class="tagline" style="top:199px;">london property finders and search agents</p>
  </section>

  <!-- Black letterhead -->
  <section class="sheet mono" style="left:594px;top:425px;width:584px;height:756px;">
    <div class="band" style="top:0;height:91px;"></div>
    <p class="wordmark" style="left:25px;top:32px;font-size:23px;">BRAMWELL PROPERTY FINDERS</p>
    <div class="rule" style="top:93px;"></div>
    <div class="contacts" style="right:34px;top:628px;">
      <p><b>t:</b> 0208 394 2860</p>
      <p><b>m:</b> +44(0)7932 418 507</p>
      <p><b>e:</b> info@bramwellpropertyfinders.co.uk</p>
      <p><b>w:</b> bramwellpropertyfinders.co.uk</p>
    </div>
    <div class="rule" style="top:698px;"></div>
    <div class="band" style="top:702px;height:54px;"></div>
    <div class="footer-text" style="top:713px;">
      <p>Kestrand Holdings Ltd Trading as Bramwell Property Finders, a company registered in England &amp; Wales, No.7351926</p>
      <p>Registered office is 41 Hollinmoor Court, Hollinmoor Road, London, SW9 3PL,</p>
      <p><b style="color:var(--sky);font-weight:700;">t:</b> 0208 394 2860, <b style="color:var(--sky);font-weight:700;">m:</b> +44(0)7932 418 507, <b style="color:var(--sky);font-weight:700;">e:</b> info@bramwellpropertyfinders.co.uk</p>
    </div>
  </section>

  <!-- Black business card, front -->
  <section class="card mono-face" style="left:25px;top:810px;width:392px;height:224px;">
    <p class="wordmark" style="left:50px;top:100px;font-size:19px;">BRAMWELL PROPERTY FINDERS</p>
  </section>

  <!-- Black business card, back -->
  <section class="card mono" style="left:170px;top:954px;width:393px;height:224px;">
    <p class="wordmark card-mark" style="left:25px;top:40px;font-size:14px;">BRAMWELL PROPERTY FINDERS</p>
    <p class="holder" style="left:25px;top:90px;">OWEN BRAMWELL</p>
    <div class="card-contacts" style="left:25px;top:114px;">
      <p><b>t:</b> 0208 394 2860</p>
      <p><b>m:</b> +44(0)7932 418 507</p>
      <p><b>e:</b> info@bramwellpropertyfinders.co.uk</p>
      <p><b>w:</b> bramwellpropertyfinders.co.uk</p>
    </div>
    <div class="rule" style="top:187px;"></div>
    <div class="band" style="top:190px;height:34px;"></div>
    <p class="tagline" style="top:201px;">london property finders and search agents</p>
  </section>

</main>
</body>
</html>
```